Amber Ladle Wishes Website Design; Cupcake Business with a unique and bespoke design element

We need a website design for a new bespoke and unique business making gourmet cupcakes - but MOST IMPORTANTLY we design and handmake cupcake wrappers and toppers specifically for each client's event. We are based in Sydney, Australia. The final resulting website should be elegant yet whimsical reflecting the notion of dreams and very elegant events eg weddings and very special parties.

We want to eventually have about 5 pages, HOWEVER, this project is specifically for the first page (ie Home page) and one other only. The final required pages are: a HOME page; ABOUT US page; PHOTO GALLERY page; FLAVOUR MENU & OTHER PRODUCTS page; CONTACT & INTERNET ENQUIRY page.

We expect the HOME page to be quite elaborate, perhaps including some animation. We will be providing the text content for all the other pages, and basically they will have the same background as the home page. We are looking for a clean design that runs across each page thus giving the website a continuity that pulls it all together. We would like our logo to be included on each page.

PLEASE NOTE: We will want multiple pages worked on in the handover phase but initially we want a very concise, consistent template to limit the amount of work to prospective designers.

While we are primarily looking for the design phase to be covered by this project, we would certainly appreciate coding to be included and will take that into consideration when choosing a winner.

Hi Designers

We have added some more information to our brief - please review it.

Thanks and happy designing

Hi Designers

Please note that we have increased our Prize money to $750.00.  We hope this encourages you to participate.

Thanks and regards
Amber Ladle Wishes

Hi Designers

We've just posted some photos to help give you an idea of what we do.  Please note our attention to detail and precision in our work.

Thanks
Amber Ladle Wishes

Hi Designers

Please Note:  What makes us different  to any other cupcake business is that we design cupcake wrappers and toppers, unique to our client's event whether it be a wedding, a birthday party or product launch.  We consult with our client to understand themes, colours, styles etc.  We then have our designs printed, next they are cut by a specialised computerised cutting machine,  We assemble everything by hand, and usually embellish the wrapper and topper with pearls, crystals, feathers, lace, ribbons or whatever else is appropriate for the event.  All work is totally bespoke, unique and individual.  No other cupcake supplier that we know of goes to these lengths to satisfy their client's dreams.

THE WRAPPER AND TOPPER IS OUR PRIMARY SELLING POINT. 

PLEASE NOTE:- We have uploaded a new photograph which we want to be used as the main photograph on the landing page.

We have removed all previous photographs of cupcakes (except for one that we can't get rid of).

We don't want a picture of a cupcake on the landing page we want the image _D7C3239.jpg to be used for that purpose.

We have also uploaded our logo in a number of file formats as we have had requests from you for these.

Hi designers

we have a crazy busy weekend on and won't be able to make any decisions re our competition until Monday  -  sorry to keep you in suspense, just a couple more days please!

regards
Meg

Target Market(s)

Primarily women - brides, new mothers (Christenings), Event Planners, who place an emphasis on the beauty of a product rather than the cost

Industry/Entity Type

Events

Requirements
Must have
• It must have our Logo (see attached upload) on each page (our logo is a butterfly atop a cupcake resting on a spoon and our motto is "Creating Delicious Works of Art". The colours used are pale pink, blue and chocolate brown and we'd expect these colours to be repeated in the final website.
The website must have a photo gallery which we can access and add to/change as our business grows.
We need a contact page which has an "internet enquiry form".
There should be a "Menu" page describing our cupcake flavours.
The Home page must have a party/event feel to it - definitely making an enquirer want to enter further into the site.
Nice to have
• Our logo is attached below in the "uploads". One idea that we have had is to use the butterfly in the logo but start it as a caterpillar crawling on the screen; as it spins it's cocoon the words "Sweet Dreams Little Caterpillar" would appear on screen; this would incorporate the "Dreams" in our Business Name; then our logo butterfly would hatch. This encapsulates the idea of taking something plain (caterpillar/cupcake) and creating something beautiful (butterfly/OUR cupcake).
However, we are open to other design ideas.
The colours we would like to have are pale pink, blue and chocolate brown in the design.

Some websites we really admire are: www.dorawillow.com www.thimblereedtart.com.au and www.greetingsvera.com.au
These websites have a lightness and sense of fantasy to them. They do not convey a corporate image at all, rather they make you want to be at the party.
Should not have
• No "Corporate" style.

Most Important: We already have a website which we are not happy with - that is why we are going through this exercise to replace it. That means we DO NOT want anything along the lines of our current website. We are expecting some fresh ideas for our prize money.

```html
<!DOCTYPE html>
<html lang="en">
<head>
<meta charset="utf-8">
<title>Amber Ladle Wishes</title>
<link rel="stylesheet" href="https://fonts.googleapis.com/css2?family=Fondamento&family=Great+Vibes&family=Mulish:wght@400;600&display=swap">
<style>
:root{
  --bg:#f6ccd1;
  --page:#f9d9dd;
  --brown:#5a2f37;
  --brown-dark:#4a242c;
  --brown-text:#5a3a1e;
  --pink-strong:#e0185e;
  --pink-box:#f5a7ac;
  --blue-box:#6a9fc7;
  --blue-text:#3d6f98;
  --body-text:#4a3a34;
  --white:#ffffff;
}
*{box-sizing:border-box;margin:0;padding:0}
html,body{width:1200px;height:1025px;overflow:hidden}
body{background:var(--bg);font-family:"Mulish",sans-serif;color:var(--body-text);position:relative}
.page{position:absolute;left:155px;top:0;width:890px;height:1025px;background:var(--page);box-shadow:0 0 12px rgba(150,80,90,.25)}
.search{position:absolute;left:773px;top:14px;display:flex;align-items:center;font-size:14px;color:#5b4a4a}
.search-field{width:165px;height:24px;background:#a98d93;border:1px solid #7e6167;margin-left:10px}
.search-go{width:28px;height:24px;background:#6aaad6;color:var(--white);font-size:13px;display:flex;align-items:center;justify-content:center;margin-left:4px}
.ribbon-end{position:absolute;top:64px;width:80px;height:42px;background:var(--brown-dark)}
.ribbon-end.left{left:70px;clip-path:polygon(0 50%,14% 0,100% 0,100% 100%,14% 100%)}
.ribbon-end.right{left:1052px;clip-path:polygon(0 0,86% 0,100% 50%,86% 100%,0 100%)}
.nav{position:absolute;left:122px;top:51px;width:956px;height:45px;background:var(--brown);border:3px solid #6f434b;box-shadow:0 5px 8px rgba(60,20,30,.4)}
.nav a{position:absolute;top:8px;font-family:"Fondamento",cursive;color:var(--white);text-decoration:none;font-size:14px;line-height:23px;white-space:nowrap}
.nav a.current{background:#3d1c22;border-radius:2px;padding:0 18px}
.header{position:absolute;left:155px;top:96px;width:890px;height:290px}
.brand{position:absolute;left:68px;top:205px;font-weight:600;font-size:40px;color:var(--brown-text);display:flex;align-items:center;gap:12px;white-space:nowrap}
.brand-dot{width:14px;height:14px;border-radius:50%;background:var(--pink-strong)}
.hero-cupcake{position:absolute;left:697px;top:113px;width:180px;height:195px;border-radius:45% 45% 20% 20%;background:radial-gradient(circle at 50% 28%,#fbf3ea 0 30%,#6b3b2a 42%,#23202a 75%)}
.scallop-band{position:absolute;left:146px;top:383px;width:910px;height:90px}
.welcome{position:absolute;left:178px;top:497px;font-family:"Great Vibes",cursive;font-size:33px;color:var(--blue-text);font-weight:400;white-space:nowrap}
.lead-pink{position:absolute;left:179px;top:550px;font-size:12px;color:var(--pink-strong)}
.lead-brown{position:absolute;left:179px;top:569px;font-size:12px;color:var(--brown-text)}
.intro{position:absolute;left:179px;top:595px;width:565px;font-size:10.5px;line-height:16px;letter-spacing:-.1px}
.why{position:absolute;left:178px;top:710px;font-size:22px;font-weight:400;color:var(--blue-text)}
.why-lead{position:absolute;left:182px;top:747px;width:545px;font-size:12px;line-height:16px;color:var(--pink-strong)}
.feature{position:absolute;top:795px;display:flex;gap:5px}
.feature-photo{width:132px;height:105px;border:1px solid #8b6b6b;background:#fff;padding:4px;border-radius:2px;flex:none}
.feature-photo span{display:block;width:100%;height:100%}
.feature h3{font-size:12px;font-weight:400;color:var(--brown-text);margin-top:4px;white-space:nowrap}
.feature p{font-size:11px;line-height:16px;width:146px;margin-top:3px}
.side-box{position:absolute;left:761px;width:265px;color:var(--white);border-radius:3px;padding:26px 0 0 40px}
.side-box h2{font-size:22px;font-weight:400}
.featured{top:493px;height:238px;background:var(--pink-box)}
.featured .intro-line{font-size:11px;line-height:16px;color:#2a1a1a;margin-top:6px;width:224px;letter-spacing:-.2px}
.featured-photo{position:absolute;left:38px;top:112px;width:98px;height:108px;border-radius:40% 40% 25% 25%;background:radial-gradient(circle at 50% 30%,#f3e6e6 0 22%,#b43d52 35%,#6a2a3a 75%)}
.featured ul{position:absolute;left:157px;top:108px;list-style:none;width:90px}
.featured li{font-size:10.5px;border-bottom:1px dashed rgba(255,255,255,.7);padding:3px 2px 5px;white-space:nowrap}
.standard{top:735px;height:150px;background:var(--blue-box)}
.chef-photo{position:absolute;left:39px;top:58px;width:90px;height:80px;border:2px solid #fff;background:linear-gradient(160deg,#b78a6d,#e6d8cf)}
.standard p{position:absolute;left:136px;top:63px;width:122px;font-size:11px;line-height:16px}
.standard a{position:absolute;left:139px;top:115px;font-size:10px;color:var(--white)}
.connect{position:absolute;left:773px;top:903px;display:flex;align-items:center;gap:7px;font-size:11px;color:#4a4a4a}
.connect .label{margin-right:6px}
.social{width:20px;height:20px;border-radius:2px}
.footer-band{position:absolute;left:45px;top:936px;width:1111px;height:65px;background:var(--brown-dark)}
.footer{position:absolute;left:147px;top:943px;width:906px;height:64px;background:var(--brown);text-align:center;color:var(--white);font-size:11px}
.footer nav{margin-top:14px}
.footer nav a{color:var(--white);text-decoration:none;margin:0 3px}
.footer p{margin-top:9px}
</style>
</head>
<body>
<div class="page"></div>

<form class="search">Search <span class="search-field"></span><span class="search-go">Go</span></form>

<div class="ribbon-end left"></div>
<div class="ribbon-end right"></div>
<nav class="nav">
  <a class="current" href="#" style="left:118px">Home</a>
  <a href="#" style="left:229px">About Us</a>
  <a href="#" style="left:331px">Photo gallery</a>
  <a href="#" style="left:455px">Flavor Menu</a>
  <a href="#" style="left:579px">Products</a>
  <a href="#" style="left:675px">Contact</a>
  <a href="#" style="left:765px">Enquiry</a>
</nav>

<header class="header">
  <div class="brand"><span class="brand-dot"></span>Amber Ladle Wishes</div>
  <div class="hero-cupcake" role="img" aria-label="Photo of a chocolate cupcake with cream frosting"></div>
</header>

<svg class="scallop-band" viewBox="0 0 910 90" aria-hidden="true">
  <defs>
    <linearGradient id="band" x1="0" y1="0" x2="0" y2="1">
      <stop offset="0" stop-color="#f9c8cd"/><stop offset="1" stop-color="#f6b3ba"/>
    </linearGradient>
    <pattern id="scallop" width="14" height="10" patternUnits="userSpaceOnUse">
      <circle cx="7" cy="0" r="7" fill="#f6b3ba"/>
    </pattern>
  </defs>
  <path d="M8 0 H902 L910 76 H0 Z" fill="url(#band)"/>
  <rect x="0" y="76" width="910" height="9" fill="url(#scallop)"/>
  <line x1="0" y1="76" x2="910" y2="76" stroke="#f0a8b0" stroke-width="1"/>
</svg>

<main>
  <h1 class="welcome">Welcome to Amber Ladle Wishes!</h1>
  <p class="lead-pink">These cases are perfectly simple and easy to distinguish.</p>
  <p class="lead-brown">The wise man therefore always holds in these matters to this principle of selection:</p>
  <p class="intro">These cases are perfectly simple and easy to distinguish. In a free hour, when our power of choice is untrammelled and when nothing prevents our being able to do what we like best, every pleasure is to be welcomed and every pain avoided. But in certain circumstances and owing to the claims of duty or the obligations of business it will frequently occur that pleasures have to be repudiated and annoyances accepted. The wise man therefore always holds in these matters to this principle of selection: he rejects pleasures to secure other greater pleasures, or else he endures pains to avoid worse pains</p>

  <h2 class="why">Why choose us our bakery?</h2>
  <p class="why-lead">These cases are perfectly simple and easy to distinguish.n a free hour, when our power of choice is untrammelled and when nothing prevents</p>

  <article class="feature" style="left:185px">
    <div class="feature-photo"><span role="img" aria-label="Photo of a tiered stand of pink decorated cupcakes" style="background:linear-gradient(180deg,#f4e8ea,#e98aa0 60%,#c45a73)"></span></div>
    <div><h3>At vero eos et accusamus</h3><p>Temporibus autem quibus-dam et aut officiis debitis aut rerum necessitatibus saepe eveniet ut et voluptates repudiandae .</p></div>
  </article>
  <article class="feature" style="left:470px">
    <div class="feature-photo"><span role="img" aria-label="Photo of a cupcake with white frosting and a butterfly topper" style="background:radial-gradient(circle at 50% 45%,#f6f1ea 0 30%,#c9a23a 42%,#3a2a22 75%)"></span></div>
    <div><h3>At vero eos et accusamus</h3><p>Temporibus autem quibus-dam et aut officiis debitis aut rerum necessitatibus saepe eveniet ut et voluptates repudiandae .</p></div>
  </article>
</main>

<aside>
  <section class="side-box featured">
    <h2>Featured Category</h2>
    <p class="intro-line">The wise man therefore always holds in these matters to this principle of selection:</p>
    <div class="featured-photo" role="img" aria-label="Photo of a chocolate cupcake with a flower topper"></div>
    <ul><li>greater pleasures</li><li>greater pleasures</li><li>greater pleasures</li><li>greater pleasures</li><li>greater pleasures</li></ul>
  </section>
  <section class="side-box standard">
    <h2>Our Standard</h2>
    <div class="chef-photo" role="img" aria-label="Portrait photo of the head baker"></div>
    <p>The wise man therefore always holds in these matters to this principle</p>
    <a href="#">more</a>
  </section>
  <div class="connect"><span class="label">Connect with us:</span>
    <span class="social" style="background:#3b5b98"></span>
    <span class="social" style="background:#5fc3e8"></span>
    <span class="social" style="background:#f07b2a"></span>
    <span class="social" style="background:#1e6fa6"></span>
    <span class="social" style="background:#4c9f48"></span>
  </div>
</aside>

<div class="footer-band"></div>
<footer class="footer">
  <nav><a href="#">Home</a> | <a href="#">About Us</a> | <a href="#">Photo gallery</a> | <a href="#">Flavor Menu</a> | <a href="#">Products</a> | <a href="#">Contact</a> | <a href="#">Enquiry</a></nav>
  <p>© copyrights amber ladle wishes.All rights Reserved</p>
</footer>
</body>
</html>
```